Real Estate Development Sign

I am trying to get some good graphic design help for a new real estate development project. We need two designs for two separate large billboard-type directionals, also For Sale Signs, and also bandit directional signs. I have a company who have already given it a shot, but I don't like what they have come up with. I need it to have a WOW factor and pop to catch people's eye, but also simple and easy to read. I've attached what they have done so far. I have proofs of what has already been created and I've attached them. I've also attached the logo for the project, but I'm fine with changing the color for the logo to help make the overall signs more cohesive. I want clean, easy to read and eye catching. I will need to be able to pass the designs on to a company to have them printed for the billboards. One of them is 10x12 and the other is 8x10. Time is of the essence - I've spent too much time trying to get this other company to do what I want.
Updates

Project Deadline Extended
Reason: Need more submissions.

I would like to shoot for Black, Red, White and a touch of Yellow for the colors of the signs.

Industry/Entity Type

Graphic Design

```html
<!DOCTYPE html>
<html lang="en">
<head>
<meta charset="utf-8">
<title>The Grove at Cedar Crossing – Directional Sign</title>
<link rel="stylesheet" href="https://fonts.googleapis.com/css2?family=Mulish:wght@500;700&family=Arimo:wght@700&family=Archivo+Black&display=swap">
<style>
  :root {
    --page-bg: #ffffff;
    --sign-orange: #e04300;
    --sign-shadow: #7d7d7d;
    --ink-dark: #2f2f2f;
    --ink-light: #ffffff;
  }
  * { margin: 0; padding: 0; box-sizing: border-box; }
  html, body {
    width: 1200px;
    height: 1000px;
    overflow: hidden;
    background: var(--page-bg);
  }
  .canvas {
    position: relative;
    width: 1200px;
    height: 1000px;
  }
  .sign-shadow {
    position: absolute;
    left: 239px;
    top: 34px;
    width: 749px;
    height: 937px;
    background: var(--sign-shadow);
  }
  .sign {
    position: absolute;
    left: 233px;
    top: 28px;
    width: 749px;
    height: 937px;
    background: var(--sign-orange);
    border: 1px solid #5a2000;
  }
  .project-name {
    position: absolute;
    left: 40px;
    top: 90px;
    width: 669px;
    text-align: center;
    font-family: "Mulish", sans-serif;
    font-weight: 700;
    font-size: 58px;
    line-height: 1.15;
    letter-spacing: 1px;
    color: var(--ink-light);
  }
  .direction-arrow {
    position: absolute;
    left: 266px;
    top: 330px;
    width: 218px;
    height: 275px;
  }
  .tagline {
    position: absolute;
    left: 0;
    top: 646px;
    width: 749px;
    text-align: center;
    font-family: "Mulish", sans-serif;
    font-weight: 500;
    font-size: 49px;
    letter-spacing: 1px;
    color: var(--ink-dark);
  }
  .builder {
    position: absolute;
    left: 0;
    top: 706px;
    width: 749px;
    text-align: center;
    font-family: "Mulish", sans-serif;
    font-weight: 500;
    font-size: 32px;
    color: var(--ink-light);
  }
  .phone {
    position: absolute;
    left: 0;
    top: 758px;
    width: 749px;
    text-align: center;
    font-family: "Arimo", sans-serif;
    font-weight: 700;
    font-size: 76px;
    letter-spacing: 3px;
    word-spacing: 18px;
    color: var(--ink-light);
  }
  .status {
    position: absolute;
    left: 0;
    top: 852px;
    width: 749px;
    text-align: center;
    font-family: "Archivo Black", sans-serif;
    font-size: 56px;
    color: var(--ink-dark);
  }
</style>
</head>
<body>
<div class="canvas">
  <div class="sign-shadow"></div>
  <div class="sign">
    <div class="project-name">The Grove at<br>Cedar Crossing</div>

    <svg class="direction-arrow" viewBox="0 0 218 275" aria-hidden="true">
      <path fill="var(--ink-light)" d="
        M 109 0
        C 92 0 80 12 71 24
        L 10 110
        C -8 136 0 160 41 162
        L 41 244
        C 41 260 58 274 78 274
        L 140 274
        C 160 274 176 260 176 244
        L 176 162
        C 218 160 226 136 208 110
        L 148 24
        C 138 12 126 0 109 0 Z"/>
    </svg>

    <div class="tagline">CUSTOM GARDEN HOMES</div>
    <div class="builder">BY BRAYFIELD HOMES</div>
    <div class="phone">512 555 0148</div>
    <div class="status">Now Selling</div>
  </div>
</div>
</body>
</html>
```